Business Card needed for Drainor, a growing Septic Service company

Drainor, a growing local septic service company in Pennsylvania, needs updated business cards. We'd like the business card to feature our logo and communicate that we provide Septic Pumping, Installations/Repairs, Restroom Rentals, and 24/7 Emergency Service. The business card should be eye-catching, bold, and clean/simple. We have been in business almost 10 years and would like to expand and update our business brand and image.

Target Market(s)

Residential and Commercial, New and Current Homeowners

Industry/Entity Type

Service

Contact Information for Business Card

Contact on the business card should be: Dean Harlow Owner & Operator
Phone: 610-555-0187
Email: service@drainor-example.com
Website: www.drainor-example.com
Address: 812 Millbrook Lane Easton PA 18042

Font styles to use
Sans Serif

Colors

Designer to choose colors to be used in the design.

Requirements
Must have
• Feature logo on both side of business card.
Nice to have
• We envision the contact information on one side and our services listed on the other side. Utilize the green from the symbol in our logo as part of the design, overall design color scheme should be white, grey, black.

```html
<!DOCTYPE html>
<html lang="en">
<head>
<meta charset="utf-8">
<title>Drainor Business Card</title>
<link rel="stylesheet" href="https://fonts.googleapis.com/css2?family=Arimo:wght@400;700&display=swap">
<style>
  :root {
    --brand-green: #86c440;
    --ink-black: #050708;
    --paper-white: #ffffff;
  }
  html, body {
    margin: 0;
    padding: 0;
    overflow: hidden;
    background: var(--paper-white);
  }
  .card {
    position: relative;
    width: 1200px;
    height: 686px;
    overflow: hidden;
    background: var(--paper-white);
    font-family: "Arimo", Arial, sans-serif;
    color: var(--ink-black);
  }
  .band-top {
    position: absolute; left: 0; top: 0;
    width: 100%; height: 25px;
    background: var(--ink-black);
  }
  .brand {
    position: absolute; left: 14px; top: 46px;
    display: flex; align-items: center;
    height: 146px;
  }
  .brand-square {
    width: 146px; height: 146px;
    background: var(--brand-green);
  }
  .brand-name {
    margin-left: 24px;
    font-weight: 700;
    font-size: 132px;
    line-height: 1;
    letter-spacing: 2px;
    color: var(--ink-black);
    text-transform: uppercase;
  }
  .rule-green {
    position: absolute; left: 0; top: 207px;
    width: 100%; height: 17px;
    background: var(--brand-green);
  }
  .contact-list {
    position: absolute; left: 14px; top: 289px;
    margin: 0; padding: 0; list-style: none;
  }
  .contact-item {
    display: flex; align-items: center;
    height: 45px;
    margin-bottom: 14px;
    font-size: 43px;
    line-height: 1;
  }
  .contact-icon {
    width: 45px; height: 45px;
    flex: none;
    margin-right: 16px;
  }
  .band-bottom-black {
    position: absolute; left: 0; top: 533px;
    width: 100%; height: 26px;
    background: var(--ink-black);
  }
  .band-bottom-green {
    position: absolute; left: 0; top: 559px;
    width: 100%; height: 127px;
    background: var(--brand-green);
  }
</style>
</head>
<body>
<div class="card">
  <div class="band-top"></div>

  <div class="brand">
    <div class="brand-square"></div>
    <div class="brand-name">Drainor</div>
  </div>

  <div class="rule-green"></div>

  <ul class="contact-list">
    <li class="contact-item">
      <svg class="contact-icon" viewBox="0 0 45 45" aria-hidden="true">
        <rect width="45" height="45" rx="6" fill="#86c440"/>
        <path d="M13 9c2-1 4 0 5 2l2 5c1 2 0 3-1 4l-2 2c1 3 4 6 7 7l2-2c1-1 2-2 4-1l5 2c2 1 3 3 2 5l-1 3c-1 2-3 3-6 2C19 35 10 26 8 17c-1-3 0-5 2-6z" fill="#050708"/>
      </svg>
      <span>610-555-0187</span>
    </li>
    <li class="contact-item">
      <svg class="contact-icon" viewBox="0 0 45 45" aria-hidden="true">
        <rect width="45" height="45" rx="6" fill="#86c440"/>
        <rect x="7" y="12" width="31" height="21" fill="none" stroke="#050708" stroke-width="2"/>
        <path d="M7 12l15.5 12L38 12M7 33l12-11M38 33L26 22" fill="none" stroke="#050708" stroke-width="2"/>
      </svg>
      <span>service@drainor-example.com</span>
    </li>
    <li class="contact-item">
      <svg class="contact-icon" viewBox="0 0 45 45" aria-hidden="true">
        <rect width="45" height="45" rx="6" fill="#86c440"/>
        <path d="M14 7v28l7-6 5 10 4-2-5-10h9z" fill="#050708"/>
      </svg>
      <span>www.drainor-example.com</span>
    </li>
    <li class="contact-item">
      <svg class="contact-icon" viewBox="0 0 45 45" aria-hidden="true">
        <rect width="45" height="45" rx="6" fill="#86c440"/>
        <path d="M22.5 40C16 31 11 24 11 18a11.5 11.5 0 0 1 23 0c0 6-5 13-11.5 22z" fill="#050708"/>
        <circle cx="22.5" cy="18" r="5" fill="#ffffff"/>
      </svg>
      <span>812 Millbrook Lane Easton PA 18042</span>
    </li>
  </ul>

  <div class="band-bottom-black"></div>
  <div class="band-bottom-green"></div>
</div>
</body>
</html>
```